Wordpress website design for Tavi Linkway-Africa

We need a website for a new consultancy and digital marketplace in Kenya called 'Tavi Linkway - Africa'. Please refer to the the attached document [Tavi Linkway Africa website brief] and contact me anytime.

Bests,
Philippa

Deadline extended to allow for additional revisions and refinements, ensuring that final designs align closely with project objectives and quality standards. This extra time will help incorporate valuable feedback and ensure the final output meets our high expectations.

```html
<!DOCTYPE html>
<html lang="en">
<head>
<meta charset="utf-8">
<title>Tavi Linkway – Templates</title>
<link href="https://fonts.googleapis.com/css2?family=Playfair+Display:wght@600&family=Poppins:wght@400;500;600;700&display=swap" rel="stylesheet">
<style>
:root{
  --navy:#18213f;
  --green:#12d40f;
  --ink:#141414;
  --line:#1c2541;
  --white:#ffffff;
  --muted:#d8dbe5;
  --rule:#2c365a;
  --card-shadow:0 1px 4px rgba(0,0,0,.10);
}
*{box-sizing:border-box;margin:0;padding:0}
html,body{width:848px;height:1200px;overflow:hidden;background:var(--white)}
body{font-family:'Poppins',sans-serif;color:var(--ink);position:relative}

.site-header{position:absolute;left:0;top:0;width:848px;height:59px;background:var(--navy)}
.brand{position:absolute;font-family:'Playfair Display',serif;font-weight:600;color:var(--white);font-size:26px;line-height:1;white-space:nowrap}
.site-header .brand{left:100px;top:16px}
.nav-link{position:absolute;top:23px;color:var(--white);font-size:11px;font-weight:500;line-height:14px;white-space:nowrap}
.donate{position:absolute;left:630px;top:21px;width:57px;height:21px;background:var(--green);color:var(--navy);font-size:8.5px;font-weight:600;display:flex;align-items:center;justify-content:center;letter-spacing:.3px}
.cart{position:absolute;left:738px;top:25px}
.cart-count{position:absolute;left:746px;top:22px;width:10px;height:10px;border-radius:50%;background:var(--green);color:var(--navy);font-size:6px;display:flex;align-items:center;justify-content:center}

.filter-title{position:absolute;left:17px;font-size:9.5px;font-weight:700;color:var(--navy);line-height:12px;white-space:nowrap}
.filter-arrow{position:absolute;left:128px}
.filter-rule{position:absolute;left:14px;width:130px;height:1.2px;background:var(--line)}
.cat-item{position:absolute;left:17px;font-size:8.5px;line-height:11px}
.cat-item.active{color:var(--green);text-decoration:underline}

.page-title{position:absolute;left:176px;top:79px;font-size:14.5px;font-weight:600;color:var(--navy);line-height:18px}
.count{position:absolute;left:177px;top:98px;font-size:8.5px;line-height:11px}
.sort-label{position:absolute;left:661px;top:87px;font-size:8.5px;font-weight:500;line-height:11px}
.sort-select{position:absolute;left:701px;top:84px;width:133px;height:28px;border:1px solid var(--navy);font-size:8.5px;padding:0 9px 0 9px;display:flex;align-items:center;justify-content:space-between}

.product-grid{position:absolute;left:181px;top:138px;display:grid;grid-template-columns:repeat(4,153px);column-gap:14px;row-gap:14px}
.product-card{height:256px;background:var(--white);box-shadow:var(--card-shadow);display:flex;flex-direction:column;align-items:center;text-align:center}
.product-thumb{width:153px;height:110px;flex:none}
.product-title{margin-top:15px;font-size:9px;font-weight:500;line-height:14px;width:130px}
.product-desc{margin-top:3px;font-size:7.8px;line-height:11.5px;width:140px}
.price{margin-top:7px;font-size:12.5px;font-weight:500;line-height:16px}
.shop-btn{margin-top:8px;width:68px;height:22px;background:var(--green);color:var(--white);font-size:8.5px;font-weight:600;display:flex;align-items:center;justify-content:center}

.site-footer{position:absolute;left:0;top:973px;width:848px;height:227px;background:var(--navy);color:var(--white)}
.site-footer .brand{left:106px;top:33px}
.follow{position:absolute;left:140px;width:100px;top:84px;text-align:center;font-size:9px;font-weight:500}
.socials{position:absolute;left:137px;top:106px;display:flex;gap:2.5px}
.socials span{width:19px;height:19px;border-radius:50%;background:var(--white)}
.foot-col{position:absolute;top:34px}
.foot-col h4{font-size:11.5px;font-weight:700;letter-spacing:.2px;margin-bottom:6px;white-space:nowrap}
.foot-col li{list-style:none;font-size:8.8px;line-height:14.8px;padding-left:1px}
.email-box{position:absolute;left:560px;top:61px;width:182px;height:29px;background:var(--white);color:var(--navy);font-size:8.5px;display:flex;align-items:center;padding-left:10px;gap:8px}
.subscribe{position:absolute;left:560px;top:99px;width:182px;height:29px;background:var(--green);color:var(--navy);font-size:11px;font-weight:700;display:flex;align-items:center;justify-content:center;letter-spacing:.3px}
.foot-rule{position:absolute;left:106px;top:157px;width:638px;height:1px;background:var(--rule)}
.payments{position:absolute;left:106px;top:185px;display:flex;gap:10px;align-items:center}
.payments span{font-size:8.5px;font-weight:600;color:var(--white);line-height:11px}
.copyright{position:absolute;right:104px;top:186px;font-size:8.3px;color:var(--muted)}
</style>
</head>
<body>
<header class="site-header">
  <div class="brand">Tavi Linkway</div>
  <span class="nav-link" style="left:337px">Home</span>
  <span class="nav-link" style="left:393px">Services</span>
  <span class="nav-link" style="left:457px">Marketplace</span>
  <span class="nav-link" style="left:541px">About Us</span>
  <span class="nav-link" style="left:610px">Contact</span>
  <div class="donate" style="left:668px;top:22px;width:60px;height:22px">DONATE</div>
  <svg class="cart" width="14" height="13" viewBox="0 0 14 13" fill="none" stroke="#fff" stroke-width="1.2"><path d="M0.5 1h2l2 7h7l1.5-5H3.5"/><circle cx="5.5" cy="11" r="1"/><circle cx="10.5" cy="11" r="1"/></svg>
  <div class="cart-count">0</div>
</header>

<aside class="sidebar">
  <div class="filter-title" style="top:76px">Shop by category</div>
  <svg class="filter-arrow" style="top:79px" width="10" height="6" viewBox="0 0 10 6" fill="none" stroke="#18213f"><path d="M1 5.5 5 1.5 9 5.5"/></svg>
  <div class="filter-rule" style="top:94px"></div>
  <div class="cat-item active" style="top:106px">Templates</div>
  <div class="cat-item" style="top:124px">Guides</div>
  <div class="cat-item" style="top:141px">Courses</div>
  <div class="cat-item" style="top:159px">Software</div>
  <div class="cat-item" style="top:176px">Toolkits</div>

  <div class="filter-title" style="top:207px">Features</div>
  <svg class="filter-arrow" style="top:211px" width="10" height="6" viewBox="0 0 10 6" fill="none" stroke="#18213f"><path d="M1 .5 5 4.5 9 .5"/></svg>
  <div class="filter-rule" style="top:226px"></div>
  <div class="filter-title" style="top:237px">Best for</div>
  <svg class="filter-arrow" style="top:241px" width="10" height="6" viewBox="0 0 10 6" fill="none" stroke="#18213f"><path d="M1 .5 5 4.5 9 .5"/></svg>
  <div class="filter-rule" style="top:256px"></div>
  <div class="filter-title" style="top:267px">Status</div>
  <svg class="filter-arrow" style="top:270px" width="10" height="6" viewBox="0 0 10 6" fill="none" stroke="#18213f"><path d="M1 .5 5 4.5 9 .5"/></svg>
  <div class="filter-rule" style="top:285px"></div>
  <div class="filter-title" style="top:297px">Plan type</div>
  <svg class="filter-arrow" style="top:301px" width="10" height="6" viewBox="0 0 10 6" fill="none" stroke="#18213f"><path d="M1 .5 5 4.5 9 .5"/></svg>
  <div class="filter-rule" style="top:317px"></div>
  <div class="filter-title" style="top:327px">Price range</div>
  <svg class="filter-arrow" style="top:333px" width="10" height="6" viewBox="0 0 10 6" fill="none" stroke="#18213f"><path d="M1 .5 5 4.5 9 .5"/></svg>
</aside>

<h1 class="page-title">Templates</h1>
<div class="count">12 Products</div>
<div class="sort-label">Sort by:</div>
<div class="sort-select">Recommended<svg width="10" height="6" viewBox="0 0 10 6" fill="none" stroke="#18213f"><path d="M1 .5 5 4.5 9 .5"/></svg></div>

<main class="product-grid">
  <article class="product-card"><div class="product-thumb" role="img" aria-label="Book layout shown on devices" style="background:linear-gradient(135deg,#3e3e3e,#5a5a5a)"></div><h2 class="product-title">Sed ut perspiciatis unde omnis iste natus error.</h2><p class="product-desc">Lorem ipsum dolor sit amet, cons ectetur adipiscing eli, sed.</p><div class="price">$59.00</div><div class="shop-btn">Shop Now</div></article>
  <article class="product-card"><div class="product-thumb" role="img" aria-label="Hand holding a smartphone mockup" style="background:linear-gradient(135deg,#2f3a3c,#7a4438 60%,#e0565f)"></div><h2 class="product-title">Sed ut perspiciatis unde omnis iste natus error.</h2><p class="product-desc">Lorem ipsum dolor sit amet, cons ectetur adipiscing eli, sed.</p><div class="price">$59.00</div><div class="shop-btn">Shop Now</div></article>
  <article class="product-card"><div class="product-thumb" role="img" aria-label="Website design on desktop, laptop and phone" style="background:linear-gradient(135deg,#a7c6e6,#c7b8e0 60%,#9fb7e0)"></div><h2 class="product-title">Sed ut perspiciatis unde omnis iste natus error.</h2><p class="product-desc">Lorem ipsum dolor sit amet, cons ectetur adipiscing eli, sed.</p><div class="price">$59.00</div><div class="shop-btn">Shop Now</div></article>
  <article class="product-card"><div class="product-thumb" role="img" aria-label="Mobile app screens" style="background:linear-gradient(135deg,#eeeef4,#b7a6e3 55%,#e7e6ef)"></div><h2 class="product-title">Sed ut perspiciatis unde omnis iste natus error.</h2><p class="product-desc">Lorem ipsum dolor sit amet, cons ectetur adipiscing eli, sed.</p><div class="price">$59.00</div><div class="shop-btn">Shop Now</div></article>

  <article class="product-card"><div class="product-thumb" role="img" aria-label="Landing page wireframe sheets" style="background:linear-gradient(135deg,#d6dbe2,#eef1f4 55%,#c9cfd7)"></div><h2 class="product-title">Sed ut perspiciatis unde omnis iste natus error.</h2><p class="product-desc">Lorem ipsum dolor sit amet, cons ectetur adipiscing eli, sed.</p><div class="price">$59.00</div><div class="shop-btn">Shop Now</div></article>
  <article class="product-card"><div class="product-thumb" role="img" aria-label="Fashion shop web pages" style="background:linear-gradient(135deg,#9a6fd0,#e9e2dc 50%,#f07b2a)"></div><h2 class="product-title">Sed ut perspiciatis unde omnis iste natus error.</h2><p class="product-desc">Lorem ipsum dolor sit amet, cons ectetur adipiscing eli, sed.</p><div class="price">$59.00</div><div class="shop-btn">Shop Now</div></article>
  <article class="product-card"><div class="product-thumb" role="img" aria-label="Business pitch deck slides" style="background:linear-gradient(135deg,#f2f5ea,#b9f04a 50%,#1a1a1a)"></div><h2 class="product-title">Sed ut perspiciatis unde omnis iste natus error.</h2><p class="product-desc">Lorem ipsum dolor sit amet, cons ectetur adipiscing eli, sed.</p><div class="price">$59.00</div><div class="shop-btn">Shop Now</div></article>
  <article class="product-card"><div class="product-thumb" role="img" aria-label="Laptop showing a beauty website" style="background:linear-gradient(135deg,#1f4a9a,#3567c4 55%,#1b3c80)"></div><h2 class="product-title">Sed ut perspiciatis unde omnis iste natus error.</h2><p class="product-desc">Lorem ipsum dolor sit amet, cons ectetur adipiscing eli, sed.</p><div class="price">$59.00</div><div class="shop-btn">Shop Now</div></article>

  <article class="product-card"><div class="product-thumb" role="img" aria-label="Social media post designs" style="background:linear-gradient(135deg,#a98ae8,#1a1a1a 55%,#b99af0)"></div><h2 class="product-title">Sed ut perspiciatis unde omnis iste natus error.</h2><p class="product-desc">Lorem ipsum dolor sit amet, cons ectetur adipiscing eli, sed.</p><div class="price">$59.00</div><div class="shop-btn">Shop Now</div></article>
  <article class="product-card"><div class="product-thumb" role="img" aria-label="Brand guideline pages" style="background:linear-gradient(135deg,#f4f6fa,#3b7be0 50%,#eef2f8)"></div><h2 class="product-title">Sed ut perspiciatis unde omnis iste natus error.</h2><p class="product-desc">Lorem ipsum dolor sit amet, cons ectetur adipiscing eli, sed.</p><div class="price">$59.00</div><div class="shop-btn">Shop Now</div></article>
  <article class="product-card"><div class="product-thumb" role="img" aria-label="Printed beauty magazine spreads" style="background:linear-gradient(135deg,#b9b9b7,#e8e4dc 50%,#4a4f55)"></div><h2 class="product-title">Sed ut perspiciatis unde omnis iste natus error.</h2><p class="product-desc">Lorem ipsum dolor sit amet, cons ectetur adipiscing eli, sed.</p><div class="price">$59.00</div><div class="shop-btn">Shop Now</div></article>
  <article class="product-card"><div class="product-thumb" role="img" aria-label="Minimal social layouts with phone" style="background:linear-gradient(135deg,#dedede,#efefef 55%,#e8727a)"></div><h2 class="product-title">Sed ut perspiciatis unde omnis iste natus error.</h2><p class="product-desc">Lorem ipsum dolor sit amet, cons ectetur adipiscing eli, sed.</p><div class="price">$59.00</div><div class="shop-btn">Shop Now</div></article>
</main>

<footer class="site-footer" style="top:918px;height:282px">
  <div class="brand" style="top:30px">Tavi Linkway</div>
  <div class="follow" style="top:77px">FOLLOW US</div>
  <div class="socials" style="top:100px"><span></span><span></span><span></span><span></span><span></span></div>
  <div class="foot-col" style="left:310px;top:31px"><h4>MENU</h4><ul><li>Home</li><li>Services</li><li>Marketplace</li><li>About Us</li><li>Blog</li><li>Contact</li></ul></div>
  <div class="foot-col" style="left:403px;top:31px"><h4>LOCATIONS</h4><ul><li>Msitu Rd</li><li>Kijani Park</li><li>Nairobi Kenya</li></ul></div>
  <div class="foot-col" style="left:526px;top:31px"><h4>NEWSLETTER SUBSCRIBE</h4></div>
  <div class="email-box" style="left:528px;top:58px;width:172px;height:28px"><svg width="10" height="8" viewBox="0 0 10 8"><rect width="10" height="8" rx="1" fill="#18213f"/><path d="M0.5 1 5 4.5 9.5 1" stroke="#fff" fill="none"/></svg>Email id</div>
  <div class="subscribe" style="left:528px;top:93px;width:172px;height:28px">SUBSCRIBE</div>
  <div class="foot-rule" style="left:100px;top:149px;width:602px"></div>
  <div class="payments" style="left:100px;top:176px"><span>Kivuli</span><span>Orlan</span><span>Tessel</span><span>Mbaraka</span><span>Nyota</span></div>
  <div class="copyright" style="right:146px;top:175px">Copyright © 2024 All Rights Reserved</div>
</footer>
</body>
</html>
```